Halcyon Skyways Global Business Card

I would like a professional business card designed. The plane that is being used is a Vortan Aero Ridgeline 740. Our primary business colors would be navy blue and light blue. This is a charter plane for hire. Our clients range from business people to vacation goers. A website is currently under development and two of the primary pictures being used will be attached. The pictures don't need to be used in the business card design, but could be used for inspiration and reference. We will need our P.O. Box address on the card and personal information (Name, cell number, email address, and website address (www.halcyonskywaysglobal.example)) Thanks! God Bless!
Updates

The contact info for the back of the card: Milo Dearborn Cell: 555.014.2738 Email: mdearborn@halcyonskywaysglobal.example

Target Market(s)

Business people

Industry/Entity Type

Business

Contact Information for Business Card

This will be on a standard square cornered business card.

Requirements
Must have
• Professional look

```html
<!DOCTYPE html>
<html lang="en">
<head>
<meta charset="utf-8">
<title>Halcyon Skyways Global — Business Card</title>
<link rel="stylesheet" href="https://fonts.googleapis.com/css2?family=PT+Sans:wght@400;700&family=Cinzel:wght@400;700&display=swap">
<style>
  :root {
    --backdrop: #3b3633;
    --card-front: #1d1d1f;
    --card-front-edge: #252527;
    --card-back: #151515;
    --brand-blue: #2f5fe6;
    --brand-blue-light: #3b78f0;
    --name-blue: #4a86e8;
    --text-light: #e9e9ec;
    --divider: #3a3a3d;
    --mark-grey: #6d6d70;
  }
  * { margin: 0; padding: 0; box-sizing: border-box; }
  html, body {
    width: 1200px;
    height: 844px;
    overflow: hidden;
    background: var(--backdrop);
  }
  .stage {
    width: 1200px;
    height: 844px;
    display: flex;
    align-items: center;
    justify-content: center;
    gap: 44px;
  }
  .card {
    width: 530px;
    height: 303px;
    position: relative;
    box-shadow: 0 14px 30px rgba(0,0,0,.45);
  }
  /* Front: contact side */
  .card--front {
    background: linear-gradient(135deg, var(--card-front-edge), var(--card-front));
    font-family: "PT Sans", sans-serif;
    color: var(--text-light);
  }
  .brand-badge {
    position: absolute;
    left: 36px;
    top: 76px;
    width: 150px;
    display: flex;
    flex-direction: column;
    align-items: center;
    gap: 12px;
  }
  .brand-badge__circle {
    width: 120px;
    height: 120px;
    border-radius: 50%;
    background: radial-gradient(circle at 40% 35%, var(--brand-blue-light), var(--brand-blue));
  }
  .brand-badge__name {
    font-size: 11px;
    font-weight: 400;
    color: var(--text-light);
    letter-spacing: .5px;
    white-space: nowrap;
  }
  .card__divider {
    position: absolute;
    left: 208px;
    top: 38px;
    width: 1px;
    height: 226px;
    background: var(--divider);
  }
  .contact {
    position: absolute;
    left: 228px;
    top: 58px;
    right: 14px;
  }
  .contact__name {
    font-size: 23px;
    font-weight: 400;
    color: var(--name-blue);
    line-height: 1.05;
  }
  .contact__title {
    font-size: 13px;
    margin-top: 2px;
  }
  .contact__lines {
    list-style: none;
    margin-top: 18px;
    font-size: 13px;
    line-height: 1.3;
  }
  .contact__label { color: var(--name-blue); }
  .contact__address {
    margin-top: 18px;
    font-size: 14px;
    line-height: 1.25;
    font-style: normal;
  }
  /* Back: brand side */
  .card--back {
    background: var(--card-back);
    display: flex;
    flex-direction: column;
    align-items: center;
    justify-content: center;
  }
  .wordmark {
    display: flex;
    align-items: center;
    gap: 10px;
    font-family: "Cinzel", serif;
    font-weight: 700;
    font-size: 27px;
    color: var(--mark-grey);
    white-space: nowrap;
  }
  .wordmark__circle {
    width: 30px;
    height: 30px;
    border-radius: 50%;
    background: var(--mark-grey);
  }
  .wordmark__rule {
    margin-top: 14px;
    width: 300px;
    height: 1px;
    background: var(--mark-grey);
  }
</style>
</head>
<body>
  <main class="stage">
    <section class="card card--front" aria-label="Card front with contact details">
      <div class="brand-badge">
        <div class="brand-badge__circle"></div>
        <span class="brand-badge__name">Halcyon Skyways Global</span>
      </div>
      <div class="card__divider"></div>
      <div class="contact">
        <h1 class="contact__name">Milo Dearborn</h1>
        <p class="contact__title">Managing Director</p>
        <ul class="contact__lines">
          <li><span class="contact__label">T:</span> 555.014.2738</li>
          <li><span class="contact__label">E:</span> mdearborn@halcyonskywaysglobal.example</li>
          <li><span class="contact__label">W:</span> www.halcyonskywaysglobal.example</li>
        </ul>
        <address class="contact__address">12345, Address Goes Here<br>Country Name, 123456.</address>
      </div>
    </section>

    <section class="card card--back" aria-label="Card back with company name">
      <div class="wordmark">
        <span class="wordmark__circle"></span>
        <span>Halcyon Skyways Global</span>
      </div>
      <div class="wordmark__rule"></div>
    </section>
  </main>
</body>
</html>
```